Marketing collateral for KESTA a ladies wellness center and spa
KESTA mind and body wellness
mind and body wellness
i need a design for marketing and adds
Salon & Spa
==============Update==============
I would like it to be a Tri-Fold brochure design.
Our center consists of different services we divide them into spa,
physiotherapy , psychology and dermatology. i know i can't jam in all
images in a one brochure design but give me your best at it, as for the
images from prime frame photo:
1) pebble trove 40926318
2) crimson lens cq5093416
3) choose any number of pictures i attached of our center.
this is the logo with black background
G with black background
this is the logo with WHITE background
G with WHITE background
Business Card Front
Business Card Back
Latterhead

```html
<!DOCTYPE html>
<html lang="en">
<head>
<meta charset="utf-8">
<title>KESTA mind and body wellness – collateral</title>
<link rel="stylesheet" href="https://fonts.googleapis.com/css2?family=Montserrat:wght@400;500;600;700&family=Open+Sans:wght@400;600&display=swap">
<style>
:root{
  --bg:#e9e6e1;
  --ink:#141210;
  --ink-soft:#2a2622;
  --gold:#c9a24a;
  --gold-light:#e8cd86;
  --gold-deep:#8d6a22;
  --paper:#fbf8f2;
  --text:#3b352d;
  --stone:#56585a;
}
*{box-sizing:border-box;margin:0;padding:0}
html,body{width:1200px;height:850px;overflow:hidden;background:var(--bg)}
body{position:relative;font-family:"Open Sans",sans-serif;color:var(--text)}
.piece{position:absolute;overflow:hidden;box-shadow:0 2px 8px rgba(0,0,0,.18)}
.piece svg.waves{position:absolute;inset:0;width:100%;height:100%}
.brand{font-family:"Montserrat",sans-serif;font-weight:600;color:var(--gold);letter-spacing:.12em;display:flex;align-items:center;gap:8px}
.brand .dot{width:10px;height:10px;border-radius:50%;background:var(--gold)}
.tagline{font-family:"Montserrat",sans-serif;font-size:8px;letter-spacing:.18em;text-transform:uppercase;color:var(--gold-light)}
.photo{position:absolute}
.hours{font-family:"Montserrat",sans-serif;color:var(--gold)}
.hours h3{font-weight:700;font-size:20px;letter-spacing:.04em;margin-bottom:4px}
.hours dl{display:grid;grid-template-columns:auto auto;column-gap:10px;font-size:9.5px;color:#f1e6c8;line-height:1.45}
.hours dt{font-weight:600}
.contact{font-size:8px;line-height:1.5;color:#f1e6c8}

/* business card back */
.card-back{left:30px;top:40px;width:205px;height:340px;background:var(--ink)}
.card-back .brand{position:absolute;left:20px;top:128px;font-size:24px}
.card-back .tagline{position:absolute;left:22px;top:160px}
.card-back .hours{position:absolute;left:22px;top:188px}
.card-back .contact{position:absolute;left:22px;bottom:16px}

/* business card front */
.card-front{left:250px;top:40px;width:205px;height:340px;background:var(--ink)}
.card-front .photo{left:70px;top:24px;width:110px;height:120px;border-radius:8px;background:radial-gradient(circle at 50% 40%,#7a7c7e,var(--stone) 55%,#2a2b2c)}
.card-front .brand{position:absolute;left:24px;top:250px;font-size:26px}
.card-front .tagline{position:absolute;left:26px;top:284px}

/* square card */
.square-card{left:30px;top:420px;width:425px;height:400px;background:var(--ink)}
.square-card .photo{right:0;top:0;width:230px;height:190px;background:radial-gradient(circle at 60% 45%,var(--gold-light),var(--gold) 60%,var(--gold-deep))}
.square-card .brand{position:absolute;left:36px;top:210px;font-size:44px}
.square-card .tagline{position:absolute;left:40px;top:266px;font-size:10px}
.square-card .contact{position:absolute;left:40px;top:296px;font-size:9px}

/* trifold outside */
.trifold-out{left:480px;top:40px;width:690px;height:360px;background:var(--ink);display:grid;grid-template-columns:repeat(3,1fr)}
.trifold-out .panel{position:relative;border-right:1px solid rgba(255,255,255,.06)}
.trifold-out .spa-photo{left:0;top:0;width:100%;height:240px;background:linear-gradient(180deg,#e9b63a 0%,#d8552d 35%,#f2a43b 60%,#b9a48a 100%)}
.trifold-out .hours{position:absolute;left:22px;top:30px}
.trifold-out .contact{position:absolute;left:22px;bottom:30px}
.trifold-out .stones{right:30px;top:24px;width:90px;height:130px;border-radius:8px;background:radial-gradient(circle at 50% 40%,#7a7c7e,var(--stone) 55%,#2a2b2c)}
.trifold-out .brand{position:absolute;left:28px;top:190px;font-size:30px}
.trifold-out .tagline{position:absolute;left:30px;top:230px}

/* trifold inside */
.trifold-in{left:480px;top:440px;width:690px;height:380px;background:var(--paper);display:grid;grid-template-columns:repeat(3,1fr)}
.trifold-in .panel{position:relative;padding:22px 18px 0;border-right:1px solid #e6dccb;font-size:8px;line-height:1.5}
.trifold-in p{margin-bottom:6px}
.trifold-in ul{list-style:none}
.trifold-in li{position:relative;padding-left:11px;margin-bottom:6px}
.trifold-in li::before{content:"";position:absolute;left:0;top:4px;width:5px;height:5px;background:var(--gold)}
.trifold-in h4{font-family:"Montserrat",sans-serif;font-size:9px;font-weight:700;color:var(--gold-deep);text-transform:uppercase;letter-spacing:.06em;margin:6px 0 4px}
.service-list{display:grid;grid-template-columns:1fr 1fr;gap:2px 10px}
.service-list span{font-weight:600;color:var(--ink-soft)}
.plain-list li{padding-left:0}
.plain-list li::before{display:none}
.trifold-in .brand{font-size:18px;margin-top:8px}
.fold-label{position:absolute;left:18px;bottom:14px;font-family:"Montserrat",sans-serif;font-size:8px;font-weight:600;letter-spacing:.14em;text-transform:uppercase;color:var(--gold-light);z-index:2}
.trifold-in .band{position:absolute;left:0;right:0;bottom:0;height:80px}
</style>
</head>
<body>

<!-- business card back -->
<section class="piece card-back">
  <svg class="waves" viewBox="0 0 205 340" preserveAspectRatio="none" aria-hidden="true">
    <defs><linearGradient id="gb" x1="0" y1="0" x2="1" y2="1"><stop offset="0" stop-color="#e8cd86"/><stop offset="1" stop-color="#8d6a22"/></linearGradient></defs>
    <path d="M0 0H205V70C150 120 70 95 0 120Z" fill="url(#gb)"/>
    <path d="M0 120C70 95 150 120 205 70V78C150 128 70 103 0 128Z" fill="#141210"/>
    <path d="M0 300C80 285 140 320 205 290V340H0Z" fill="url(#gb)"/>
  </svg>
  <div class="brand"><span class="dot"></span>KESTA</div>
  <div class="tagline">mind and body wellness</div>
  <div class="hours">
    <h3>HOURS</h3>
    <dl>
      <dt>Monday</dt><dd>9:00 – 4:30</dd>
      <dt>Tuesday</dt><dd>9:00 – 4:30</dd>
      <dt>Wednesday</dt><dd>9:00 – 4:30</dd>
      <dt>Thursday</dt><dd>9:00 – 4:30</dd>
      <dt>Friday</dt><dd>9:00 – 2:00</dd>
    </dl>
  </div>
  <div class="contact" style="color:#141210">hello@kesta-wellness.example</div>
</section>

<!-- business card front -->
<section class="piece card-front">
  <svg class="waves" viewBox="0 0 205 340" preserveAspectRatio="none" aria-hidden="true">
    <defs><linearGradient id="gf" x1="0" y1="0" x2="1" y2="1"><stop offset="0" stop-color="#e8cd86"/><stop offset="1" stop-color="#8d6a22"/></linearGradient></defs>
    <path d="M0 150C60 200 150 170 205 210V340H0Z" fill="url(#gf)"/>
    <path d="M0 170C60 215 150 190 205 230V340H0Z" fill="#141210"/>
  </svg>
  <div class="photo" role="img" aria-label="Stack of smooth black spa stones"></div>
  <div class="brand"><span class="dot"></span>KESTA</div>
  <div class="tagline">mind and body wellness</div>
</section>

<!-- square card -->
<section class="piece square-card">
  <svg class="waves" viewBox="0 0 425 400" preserveAspectRatio="none" aria-hidden="true">
    <defs><linearGradient id="gs" x1="0" y1="0" x2="1" y2="0"><stop offset="0" stop-color="#e8cd86"/><stop offset="1" stop-color="#8d6a22"/></linearGradient></defs>
    <path d="M0 0H200C150 60 60 90 0 100Z" fill="url(#gs)"/>
    <path d="M0 400V360C140 330 300 380 425 330V400Z" fill="url(#gs)"/>
  </svg>
  <div class="photo" role="img" aria-label="Golden frangipani flowers decoration"></div>
  <div class="brand"><span class="dot"></span>KESTA</div>
  <div class="tagline">mind and body wellness</div>
  <div class="contact">18 Amber Road, Northgate 20417<br>T +00 555 0142 880 · E hello@kesta-wellness.example</div>
</section>

<!-- trifold outside -->
<section class="piece trifold-out">
  <svg class="waves" viewBox="0 0 690 360" preserveAspectRatio="none" aria-hidden="true">
    <defs><linearGradient id="go" x1="0" y1="0" x2="1" y2="0"><stop offset="0" stop-color="#8d6a22"/><stop offset=".5" stop-color="#e8cd86"/><stop offset="1" stop-color="#8d6a22"/></linearGradient></defs>
    <path d="M0 250C90 220 170 275 230 250V360H0Z" fill="url(#go)"/>
    <path d="M0 268C90 240 170 292 230 268V360H0Z" fill="#141210"/>
    <path d="M460 280C560 240 620 300 690 260V360H460Z" fill="url(#go)"/>
    <path d="M460 300C560 262 620 318 690 282V360H460Z" fill="#141210"/>
  </svg>
  <div class="panel">
    <div class="photo spa-photo" role="img" aria-label="Folded towels with lit candles and spa stones"></div>
  </div>
  <div class="panel">
    <div class="hours">
      <h3>HOURS</h3>
      <dl>
        <dt>Monday</dt><dd>9:00 – 4:30</dd>
        <dt>Tuesday</dt><dd>9:00 – 4:30</dd>
        <dt>Wednesday</dt><dd>9:00 – 4:30</dd>
        <dt>Thursday</dt><dd>9:00 – 4:30</dd>
        <dt>Friday</dt><dd>9:00 – 2:00</dd>
      </dl>
    </div>
    <div class="contact">18 Amber Road<br>Northgate 20417<br>T +00 555 0142 880<br>hello@kesta-wellness.example</div>
  </div>
  <div class="panel">
    <div class="photo stones" role="img" aria-label="Stack of smooth black spa stones"></div>
    <div class="brand"><span class="dot"></span>KESTA</div>
    <div class="tagline">mind and body wellness</div>
  </div>
</section>

<!-- trifold inside -->
<section class="piece trifold-in">
  <svg class="waves" viewBox="0 0 690 380" preserveAspectRatio="none" aria-hidden="true">
    <defs><linearGradient id="gi" x1="0" y1="0" x2="1" y2="0"><stop offset="0" stop-color="#8d6a22"/><stop offset=".5" stop-color="#e8cd86"/><stop offset="1" stop-color="#8d6a22"/></linearGradient></defs>
    <path d="M0 320C200 290 450 350 690 300V380H0Z" fill="url(#gi)"/>
    <path d="M0 338C200 308 450 366 690 318V380H0Z" fill="#141210"/>
  </svg>
  <div class="panel">
    <p>At KESTA we believe calm begins the moment you arrive and stays long after you leave.</p>
    <ul>
      <li>Connect with our therapists who care for each guest with warmth and skill.</li>
      <li>Relax in quiet rooms designed for rest and gentle renewal.</li>
      <li>Choose from spa, physiotherapy, psychology and dermatology care in one place.</li>
      <li>Leave feeling lighter, brighter and ready for the days ahead.</li>
    </ul>
    <div class="fold-label">Your Spa Experience</div>
  </div>
  <div class="panel">
    <p>Each treatment is shaped around you, using pure oils and soft natural care.</p>
    <h4>Spa Services</h4>
    <h4 style="font-weight:500;margin-top:0">Body &amp; Skin Rejuvenation</h4>
    <div class="service-list">
      <span>Hot Stone Ritual</span><span>Hydra Facial</span>
      <span>Aroma Body Wrap</span><span>Gold Glow Facial</span>
      <span>Sea Salt Scrub</span><span>Deep Cleanse</span>
    </div>
    <div class="fold-label">Facial Treatments</div>
  </div>
  <div class="panel">
    <h4>Massage Therapy</h4>
    <ul class="plain-list">
      <li>Swedish Massage</li>
      <li>Deep Tissue</li>
      <li>Reflexology</li>
      <li>Four Hands</li>
      <li>Back &amp; Neck</li>
    </ul>
    <p>Visit us for a private tour of our center and book your first calm hour.</p>
    <div class="brand"><span class="dot"></span>KESTA</div>
  </div>
</section>

</body>
</html>
```